Fitness Equipment Repair Business Needs a Catchy New Business Card

We have an existing business card, however, it is quite plain and boring. We are expanding primarily in the commercial area (gyms, studios, apartment complexes etc). The business card will serve as eye candy to those managers/owners that can't be met for a face to face.
Originally I was planning for a brochure as well, but all of our information is better summarized on our website. (brasswheelservicing.ca).
I would like the card to match the colour scheme of the website and utilize the logo. It should have a professional clean feel to it, however, a little colouring outside the lines wouldn't hurt.
The example card is for my service technician (Corwin Haldane). If possible I would like to be able to edit the text to use for more than one person.

Industry/Entity Type

Appliance Repair

Contact Information for Business Card

Clean, crisp and professional but needs to be eye catching. Preferably using the black, white and red colour scheme matching the website. Double sided would be nice, but is not necessary.

Colors
ec1f27
ffffff
000000

Requirements
Must have
• Must be able to edit name, phone number and title to use for multiple people. Must show the company website (brasswheelservicing.ca).

```html
<!DOCTYPE html>
<html lang="en">
<head>
<meta charset="utf-8">
<title>Brass Wheel Servicing – Business Card</title>
<link rel="stylesheet" href="https://fonts.googleapis.com/css2?family=Lato:ital,wght@0,400;0,700;1,400&display=swap">
<style>
  :root {
    --stage: #e9ecef;
    --card: #1c1d21;
    --white: #ffffff;
    --red: #ec1f27;
    --ink-soft: #f2f2f2;
  }
  * { margin: 0; padding: 0; box-sizing: border-box; }
  html, body { width: 1200px; height: 900px; overflow: hidden; }
  body {
    background: var(--stage);
    font-family: "Lato", Arial, sans-serif;
    position: relative;
  }
  .business-card {
    position: absolute;
    left: 226px; top: 237px;
    width: 748px; height: 427px;
    background: var(--card);
    box-shadow: 0 10px 30px rgba(0,0,0,.25);
  }
  .brand-mark {
    position: absolute;
    left: 100px; top: 150px;
    width: 220px;
    text-align: center;
    color: var(--white);
    font-weight: 700;
    font-size: 30px;
    line-height: 1.2;
  }
  .contact-block {
    position: absolute;
    left: 395px; top: 82px;
  }
  .company-name {
    color: var(--white);
    font-weight: 700;
    font-size: 28px;
    line-height: 34px;
  }
  .person-name {
    color: var(--red);
    font-weight: 700;
    font-size: 28px;
    line-height: 34px;
    margin-bottom: 12px;
  }
  .contact-list { list-style: none; }
  .contact-item {
    display: flex;
    align-items: flex-start;
    color: var(--ink-soft);
    font-size: 19px;
    line-height: 28px;
  }
  .contact-item.gap-before { margin-top: 13px; }
  .contact-icon {
    width: 20px; height: 20px;
    margin: 4px 15px 0 0;
    flex: none;
    fill: var(--red);
  }
  .tagline {
    position: absolute;
    left: 0; right: 0; top: 376px;
    text-align: center;
    color: var(--red);
    font-style: italic;
    font-size: 18px;
  }
</style>
</head>
<body>
  <article class="business-card">
    <div class="brand-mark">Brass Wheel<br>Servicing</div>

    <div class="contact-block">
      <h1 class="company-name">Brass Wheel Servicing</h1>
      <h2 class="person-name">Corwin Haldane</h2>
      <ul class="contact-list">
        <li class="contact-item">
          <svg class="contact-icon" viewBox="0 0 24 24" aria-hidden="true"><path d="M3 8c0-3 4-5 9-5s9 2 9 5v2h-5V8c-2-1-6-1-8 0v2H3zM6 11h12l3 8H3z"/></svg>
          <span>555 014 2291</span>
        </li>
        <li class="contact-item">
          <svg class="contact-icon" viewBox="0 0 24 24" aria-hidden="true"><path d="M2 6h20v2l-10 6L2 8zM2 10l10 6 10-6v8H2z"/></svg>
          <span>brasswheel@mailhaven.com</span>
        </li>
        <li class="contact-item">
          <svg class="contact-icon" viewBox="0 0 24 24" aria-hidden="true"><path d="M10 14l4-4M8.5 12.5l-3 3a3 3 0 0 0 4 4l3-3M15.5 11.5l3-3a3 3 0 0 0-4-4l-3 3" fill="none" stroke="#ec1f27" stroke-width="2.4" stroke-linecap="round"/></svg>
          <span>www.brasswheelservicing.ca</span>
        </li>
        <li class="contact-item gap-before">
          <svg class="contact-icon" viewBox="0 0 24 24" aria-hidden="true"><rect x="6" y="1.5" width="12" height="21" rx="2" fill="none" stroke="#ec1f27" stroke-width="2"/></svg>
          <span>555 014 2291</span>
        </li>
        <li class="contact-item">
          <svg class="contact-icon" viewBox="0 0 24 24" aria-hidden="true"><path d="M12 2a7 7 0 0 0-7 7c0 5 7 13 7 13s7-8 7-13a7 7 0 0 0-7-7zm0 9.5a2.5 2.5 0 1 1 0-5 2.5 2.5 0 0 1 0 5z"/></svg>
          <span>1875 Carrow Lane NW<br>Redvale AB T4K 2P9</span>
        </li>
      </ul>
    </div>

    <p class="tagline">When your equipment can’t finish the workout, give us a call!</p>
  </article>
</body>
</html>
```